Birchwell Pantry Co - labels

I have my logo now so its time to proceed with the labels.
The product is organic juices and smoothies. They will be served in Mason jar's and sold as a premium hand made product into the CBD and outlets around Perth such as yoga studios gyms, cafe's etc. Cleanses to individuals etc.
I have attached the logo and a mock of what I would like to see.
I think the logo and the raw organic, handmade look will work with the Chalkboard design and maybe some bunting to brighten the design.
There is currently approx. 10 Juices and Smoothies to the range so I will need to settle on the design and then have you create a label for each one, once settled on the design.
If you have any questions please let me know.

Text on label:
Raw, Organic, Hand Made, Gluten-Free, Dairy-Free

Juice
Morning Tide Mix
Kale, Apple, Celery, Dandelion, Lemon & Ginger

This product is FRESH. Shake before you enjoy!!!

Label size. highest point for height 70 - 75mm. Length 200mm
I also have more wording and nutritional guide for Australian Standards. I will update soon.
Thank you

    Happy Friday Designers!!!

Well I have just increased the budget to $300. I hope this helps to get some designs coming through. If you need anything else from me please send a message.

I look forward to receiving your designs soon and thank you for working with me on my business. this is such an exciting time for me and you guys are making my dream a reality so thank you for your time.

Regards,

Denise

Reason: I have not received many designs so extending for a few more days.

• Wording - Hand Made
Raw, Organic, Gluten-Free, Dairy-Free
• A chalk board with Juice or Smoothie - Name and ingredients
Bunting I think will work well with the design of logo and chalk board plus bring some colour.

```html
<!DOCTYPE html>
<html lang="en">
<head>
<meta charset="utf-8">
<title>Birchwell Pantry Co – Juice Label</title>
<link rel="stylesheet" href="https://fonts.googleapis.com/css2?family=Cabin+Condensed:wght@400;500;600;700&display=swap">
<style>
  :root {
    --board: #231f20;
    --lime: #dce21f;
    --chalk: #ffffff;
    --page: #ffffff;
    --print: #5a5758;
  }
  html, body {
    margin: 0;
    padding: 0;
    width: 1116px;
    height: 1200px;
    overflow: hidden;
    background: var(--page);
  }
  .canvas {
    position: relative;
    width: 1116px;
    height: 1200px;
    font-family: "Cabin Condensed", "Arial Narrow", sans-serif;
  }
  .label {
    position: absolute;
    left: 177px;
    top: 252px;
    width: 408px;
    height: 645px;
    background: var(--board);
    border-radius: 14px;
  }
  .brand-seal {
    position: absolute;
    left: 234px;
    top: 144px;
    width: 286px;
    height: 286px;
    border-radius: 50%;
    background: var(--chalk);
    display: flex;
    align-items: center;
    justify-content: center;
  }
  .brand-seal__disc {
    width: 266px;
    height: 266px;
    border-radius: 50%;
    background: var(--lime);
    display: flex;
    align-items: center;
    justify-content: center;
    text-align: center;
  }
  .brand-seal__name {
    color: var(--chalk);
    font-weight: 700;
    font-size: 36px;
    line-height: 1.0;
    letter-spacing: 1px;
    text-transform: uppercase;
  }
  .label__text {
    position: absolute;
    left: 177px;
    width: 408px;
    text-align: center;
    margin: 0;
    text-transform: uppercase;
  }
  .label__range {
    top: 462px;
    color: var(--chalk);
    font-size: 54px;
    font-weight: 500;
    line-height: 1;
  }
  .label__flavour {
    top: 540px;
    color: var(--lime);
    font-size: 40px;
    font-weight: 400;
    line-height: 1;
  }
  .label__ingredients {
    top: 590px;
    color: var(--chalk);
    font-size: 25px;
    font-weight: 400;
    line-height: 32px;
  }
  .label__type {
    top: 662px;
    color: var(--lime);
    font-size: 62px;
    font-weight: 500;
    line-height: 1;
  }
  .label__claims {
    top: 845px;
    color: var(--chalk);
    font-size: 21px;
    font-weight: 400;
    line-height: 1;
  }
  .label__claims .dot { color: var(--lime); }
  .hand-print {
    position: absolute;
    left: 178px;
    top: 740px;
    width: 192px;
    height: 140px;
  }
</style>
</head>
<body>
<div class="canvas">
  <div class="label"></div>

  <svg class="hand-print" viewBox="0 0 192 140" role="img" aria-label="Faint handprint illustration pressed into the chalkboard">
    <defs>
      <radialGradient id="printFade" cx="45%" cy="45%" r="60%">
        <stop offset="0%" stop-color="#5a5758" stop-opacity="0.75"/>
        <stop offset="100%" stop-color="#5a5758" stop-opacity="0"/>
      </radialGradient>
    </defs>
    <ellipse cx="90" cy="72" rx="96" ry="66" fill="url(#printFade)"/>
  </svg>

  <div class="brand-seal">
    <div class="brand-seal__disc">
      <span class="brand-seal__name">Birchwell<br>Pantry Co</span>
    </div>
  </div>

  <p class="label__text label__range">Raw Organic</p>
  <p class="label__text label__flavour">Morning Tide Mix</p>
  <p class="label__text label__ingredients">Kale, Celery, Cucumber,<br>Lemon, Ginger</p>
  <p class="label__text label__type">Juice</p>
  <p class="label__text label__claims">Hand Made <span class="dot">•</span> Gluten-Free <span class="dot">•</span> Dairy-Free</p>
</div>
</body>
</html>
```